New Business Card

We need to refresh our business cards. We designed these ourselves and we have no graphic design experience. We would like to find a new business card design that is professional and unique. We are an auto finance company. Feel free to play with the logo, but we would like to keep the eye very present on the card. Our corporate colors are green, grey, and white.
Green - RGB - 168,215,27; HEX - #AADD22
Grey - RGB - 196,196,196; HEX - #C4C4C4
Updates
Need to upload the vector file to finalize the project. The last logo was for a jpeg that didn't stretch well.
Industry/Entity Type
Financial Service
Contact Information for Business Card
Honestly don't know...I need your help!

```html
<!DOCTYPE html>
<html lang="en">
<head>
<meta charset="utf-8">
<title>Northvale Capital – Business Card</title>
<link href="https://fonts.googleapis.com/css2?family=Arimo:wght@400;700&display=swap" rel="stylesheet">
<style>
  :root {
    --green: #a6d21b;
    --grey: #c4c4c4;
    --grey-text: #6b6b6b;
    --white: #ffffff;
    --card-white: #f7f7f7;
    --backdrop: #2c2c2e;
  }
  * { box-sizing: border-box; margin: 0; padding: 0; }
  html, body {
    width: 1200px; height: 800px; overflow: hidden;
    background: var(--backdrop);
    font-family: "Arimo", Arial, sans-serif;
  }
  .canvas { position: relative; width: 1200px; height: 800px; }
  .card {
    position: absolute; left: 320px; width: 560px; height: 320px;
    border-radius: 14px; overflow: hidden;
  }
  .card--front { top: 50px; background: var(--card-white); }
  .card--back { top: 430px; background: var(--green); }

  .band-rule {
    position: absolute; left: 0; right: 0; top: 166px; height: 6px;
    background: var(--grey);
  }
  .band {
    position: absolute; left: 0; right: 0; top: 178px; bottom: 0;
    background: var(--green);
  }

  .brand {
    position: absolute; display: flex; align-items: center; gap: 12px;
    font-weight: 700; letter-spacing: 0.5px;
  }
  .brand__dot { width: 30px; height: 30px; border-radius: 50%; }
  .card--front .brand { left: 40px; top: 62px; color: var(--green); font-size: 28px; }
  .card--front .brand__dot { background: var(--green); }

  .holder { position: absolute; right: 42px; top: 62px; text-align: right; }
  .holder__name { color: var(--green); font-weight: 700; font-size: 17px; }
  .holder__role { color: var(--grey-text); font-size: 13.5px; margin-top: 3px; }

  .address {
    position: absolute; left: 52px; bottom: 34px;
    color: var(--white); font-size: 12.5px; line-height: 1.35;
  }
  .contact {
    position: absolute; right: 38px; bottom: 32px;
    list-style: none; color: var(--white); font-size: 13px; text-align: right;
  }
  .contact__item { display: flex; justify-content: flex-end; align-items: center; gap: 8px; line-height: 19px; }
  .contact__icon { width: 12px; height: 12px; flex: none; }

  .card--back .brand {
    left: 0; right: 0; top: 0; bottom: 0; justify-content: center;
    color: var(--white); font-size: 40px;
  }
  .card--back .brand__dot { width: 44px; height: 44px; background: var(--white); }
</style>
</head>
<body>
<main class="canvas">

  <section class="card card--front" aria-label="Business card front">
    <div class="band-rule"></div>
    <div class="band"></div>

    <div class="brand"><span class="brand__dot"></span><span class="brand__name">Northvale Capital</span></div>

    <div class="holder">
      <p class="holder__name">JORDAN ELLERY</p>
      <p class="holder__role">General Manager</p>
    </div>

    <p class="address">742 Alder Ridge<br>Dr. Franklin, TN 37064</p>

    <ul class="contact">
      <li class="contact__item">555-201-4830
        <svg class="contact__icon" viewBox="0 0 12 12"><rect x="3" y="0.8" width="6" height="10.4" rx="1.3" fill="none" stroke="#fff" stroke-width="1.3"/></svg></li>
      <li class="contact__item">555-201-4831
        <svg class="contact__icon" viewBox="0 0 12 12"><path d="M2.5 1 L4.8 1 L5.5 3.6 L4.2 4.8 C5 6.6 5.9 7.5 7.2 8 L8.4 6.7 L11 7.4 L11 9.6 C6 10.5 1.5 6 2.5 1 Z" fill="#fff"/></svg></li>
      <li class="contact__item">info@northvalecap.com
        <svg class="contact__icon" viewBox="0 0 12 12"><rect x="0.7" y="2.2" width="10.6" height="7.6" fill="none" stroke="#fff" stroke-width="1.2"/><path d="M0.7 2.4 L6 6.6 L11.3 2.4" fill="none" stroke="#fff" stroke-width="1.2"/></svg></li>
      <li class="contact__item">www.northvalecap.com
        <svg class="contact__icon" viewBox="0 0 12 12"><g fill="none" stroke="#fff" stroke-width="1.1"><circle cx="6" cy="6" r="5.2"/><ellipse cx="6" cy="6" rx="2.2" ry="5.2"/><path d="M0.8 6 H11.2 M1.8 3.3 H10.2 M1.8 8.7 H10.2"/></g></svg></li>
    </ul>
  </section>

  <section class="card card--back" aria-label="Business card back">
    <div class="brand"><span class="brand__dot"></span><span class="brand__name">Northvale Capital</span></div>
  </section>

</main>
</body>
</html>
```